Plimora

We need a design for a mobile app (Android & iOS) with the following features:
- Recommend other applications based on different criteria, such as similar applications, hot apps, apps installed by friends and so on.
- Recommend a featured app everyday.
- List installed apps on the device.
- List harmful or malicious installed apps on the device
- List hot apps according to the more used apps by the comunity or the user's friends
- Profiles: Save the list of apps installed on the device as a list to allow the user to restore them on other devices.

Industry/Entity Type

Android

Requirements
Must have
• Find attached to this project a mockup of the screen elements desired.
To put it in a nutshell, the main elements are:
- Main Menu: A main menu to access the other modules of the app

- Recommended Apps: List of apps recommended, each app will display: icon, title, price, the reason(s) why it was recommended (can be expandable if takes too much room), a button to install and a button to ignore the advice.

- Application of the day: A screen that contains the icon of the app, its rating, some screenshots, a short description or promotional text, and a button to install the app. It must be also available a way to display the history and see the recommended applications the previous days.

- Installed Apps: A list with the apps on the device. It will show the app's icon, name, package, size and a button to share the app.

- Harmful apps: List of dangerous apps found on the device. It will show the icon of the app and the name. A visual and textual indicator to measure the dangerous, and the reasons of the report. It will also includes a button to ignore the advice and another one to uninstall the application.

- Login/My account: These screens will be used to login and manage the account. The account management options are listed on the attached document.

- Profiles: The design must include the proper screens and dialogs to: save a profile, restore a profile (install the missing apps on the device), show the apps saved on the profile.

- Hot Apps: The app must allow to filter between the hot apps and the hot apps installed by the user's friends. For each app, must show: the icon, name and a trending indicator in order to say if the app is winning or losing popularity

- Miscellaneous: Other features required:
+ Login screen: The login is made in two steps. First, the user introduce their email. If the email is already registered, enters the password. Otherwise, register a new account introducing a password twice (password + repeat password, please check the attached file for more info).
+ Password recovery and password change screens
+ Loading splash (shown at the start of the application for 2-4 seconds)
+ A proper layout to inform about errors / messages in empty lists, (for example if no harmful apps where found).
+ A proper layout for loading process, for example when scanning for harmful apps.
+ Vectorial App Icon: At least one icon for the app (512 x512 px)
+ Vectorial Featured (1024x500 px) and Promo banners (180x120 px) for Vexari Shop.
+ For the UI elements like buttons or checkboxes is required the following status: normal, pressed, disabled and focused.
Nice to have
• Examples of apps with nice designs:

Trendle: https://shop.vexari.example/apps/details?id=com.trendle
Quill Digest: https://shop.vexari.example/apps/details?id=com.borvik.quill
ORB Coastal Terminals: https://tunes.halvexo.example/es/app/orb-coastal-terminals/id871402965?mt=8
Should not have
• The app should not have garish or poorly contrasted colors and icons.

```html
<!DOCTYPE html>
<html lang="en">
<head>
<meta charset="utf-8">
<title>App Manager — Main Menu and Splash</title>
<link rel="stylesheet" href="https://fonts.googleapis.com/css2?family=Roboto+Condensed:wght@400;700&display=swap">
<style>
  :root {
    --page: #ffffff;
    --screen-top: #2a2a2a;
    --screen-mid: #1f1f1f;
    --screen-bottom: #161616;
    --status-bar: #3a3a3a;
    --header-top: #2c2c2c;
    --header-bottom: #050505;
    --tile-fill: #1b1b1b;
    --tile-fill-active: #141414;
    --tile-edge: #3b3b3b;
    --icon: #7c7c7c;
    --icon-dim: #5b5b5b;
    --label: #c9c9c9;
    --label-dim: #8a8a8a;
    --white: #ffffff;
  }
  * { box-sizing: border-box; margin: 0; padding: 0; }
  html, body { width: 1200px; height: 850px; overflow: hidden; background: var(--page); }
  body { position: relative; font-family: "Roboto Condensed", "Arial Narrow", sans-serif; }

  .screen {
    position: absolute;
    overflow: hidden;
    background: linear-gradient(160deg, var(--screen-top), var(--screen-mid) 55%, var(--screen-bottom));
  }
  .screen--menu { left: 38px; top: 30px; width: 520px; height: 780px; }
  .screen--splash { left: 618px; top: 32px; width: 524px; height: 783px; }

  /* status bar */
  .status-bar {
    height: 32px;
    background: linear-gradient(var(--status-bar), #222);
    color: var(--white);
    display: flex; align-items: center; justify-content: center;
    position: relative;
    font-weight: 700; font-size: 21px;
  }
  .status-bar__signal { position: absolute; left: 8px; top: 8px; }
  .status-bar__battery { position: absolute; right: 8px; top: 9px; }

  /* header */
  .app-header {
    height: 73px;
    background: linear-gradient(var(--header-top), var(--header-bottom));
    border-top: 1px solid #4a4a4a;
    display: flex; align-items: center; justify-content: center;
    box-shadow: 0 2px 6px rgba(0,0,0,.6);
  }
  .app-header__title { color: var(--white); font-size: 32px; font-weight: 400; letter-spacing: .2px; }

  /* menu tiles */
  .menu-tile {
    position: absolute; width: 152px; height: 152px;
    border-radius: 12px;
    background: var(--tile-fill);
    border: 1px solid var(--tile-edge);
    box-shadow: inset 0 1px 0 rgba(255,255,255,.05), 0 1px 2px rgba(0,0,0,.5);
    color: var(--label); text-align: center;
    font-size: 18px; line-height: 23px;
  }
  .menu-tile--active { background: var(--tile-fill-active); }
  .menu-tile--disabled { color: var(--label-dim); background: #1d1d1d; border-color: #333; }
  .menu-tile__icon {
    position: absolute; left: 0; right: 0; height: 80px;
    display: flex; align-items: center; justify-content: center;
  }
  .menu-tile__label { position: absolute; left: 0; right: 0; }

  .tile-recommended { left: 55px; top: 130px; }
  .tile-recommended .menu-tile__icon { top: 10px; }
  .tile-recommended .menu-tile__label { top: 95px; }

  .tile-of-the-day { left: 303px; top: 130px; }
  .tile-of-the-day .menu-tile__icon { top: 5px; }
  .tile-of-the-day .menu-tile__label { top: 93px; }

  .tile-installed { left: 55px; top: 323px; }
  .tile-installed .menu-tile__icon { top: 12px; }
  .tile-installed .menu-tile__label { top: 108px; }

  .tile-harmful { left: 303px; top: 323px; }
  .tile-harmful .menu-tile__icon { top: 20px; }
  .tile-harmful .menu-tile__label { top: 113px; }

  .tile-hot { left: 52px; top: 517px; }
  .tile-hot .menu-tile__icon { top: 18px; }
  .tile-hot .menu-tile__label { top: 116px; }

  /* splash */
  .splash-collage { position: absolute; left: 0; top: 0; }
  .splash-globe { position: absolute; left: 300px; top: 540px; }
  .splash-title {
    position: absolute; left: 0; right: 0; top: 304px;
    text-align: center;
    font-weight: 700; font-size: 80px; line-height: 90px;
    color: var(--white);
  }
</style>
</head>
<body>

<section class="screen screen--menu" aria-label="Main menu">
  <div class="status-bar">
    <svg class="status-bar__signal" width="32" height="16" viewBox="0 0 32 16" aria-hidden="true">
      <g fill="#fff"><rect x="0" y="12" width="4" height="4"/><rect x="6" y="9" width="4" height="7"/><rect x="12" y="6" width="4" height="10"/><rect x="18" y="3" width="4" height="13"/><rect x="24" y="0" width="4" height="16"/></g>
    </svg>
    <span class="status-bar__time">4:20 PM</span>
    <svg class="status-bar__battery" width="32" height="14" viewBox="0 0 32 14" aria-hidden="true">
      <rect x="1" y="1" width="27" height="12" rx="2" fill="none" stroke="#fff" stroke-width="1.6"/>
      <rect x="28.5" y="4.5" width="2.5" height="5" fill="#fff"/>
      <rect x="3.5" y="3.5" width="12" height="7" fill="#fff"/>
    </svg>
  </div>
  <header class="app-header"><h1 class="app-header__title">App Manager</h1></header>

  <a class="menu-tile menu-tile--active tile-recommended">
    <span class="menu-tile__icon">
      <svg width="70" height="76" viewBox="0 0 70 76" aria-hidden="true"><path fill="var(--icon)" d="M4 36h14v38H4zM22 38 L38 14 C40 6 44 2 48 4 C52 6 51 14 48 22 L46 30 H64 C68 30 70 34 68 38 C70 41 69 45 66 47 C68 50 67 54 64 56 C66 59 64 63 60 64 C61 68 58 72 54 72 H30 C26 72 22 70 22 66 Z"/></svg>
    </span>
    <span class="menu-tile__label">Recommended<br>Apps</span>
  </a>

  <a class="menu-tile tile-of-the-day">
    <span class="menu-tile__icon">
      <svg width="86" height="78" viewBox="0 0 86 78" aria-hidden="true">
        <rect x="4" y="12" width="56" height="58" rx="3" fill="none" stroke="var(--icon)" stroke-width="5"/>
        <rect x="4" y="12" width="56" height="12" fill="var(--icon)"/>
        <rect x="14" y="4" width="6" height="14" rx="2" fill="var(--icon)"/><rect x="44" y="4" width="6" height="14" rx="2" fill="var(--icon)"/>
        <text x="32" y="62" text-anchor="middle" font-family="Roboto Condensed, sans-serif" font-weight="700" font-size="30" fill="var(--icon)">17</text>
        <path fill="var(--icon)" d="M66 0 L71 12 L84 13 L74 21 L77 34 L66 27 L55 34 L58 21 L48 13 L61 12 Z"/>
      </svg>
    </span>
    <span class="menu-tile__label">Application of<br>the day</span>
  </a>

  <a class="menu-tile menu-tile--disabled tile-installed">
    <span class="menu-tile__icon">
      <svg width="72" height="76" viewBox="0 0 72 76" aria-hidden="true"><g fill="var(--icon-dim)"><path d="M36 4 L62 30 H46 V52 H26 V30 H10 Z"/><path d="M2 46 H10 V66 H62 V46 H70 V74 H2 Z"/></g></svg>
    </span>
    <span class="menu-tile__label">Installed Apps</span>
  </a>

  <a class="menu-tile tile-harmful">
    <span class="menu-tile__icon">
      <svg width="82" height="82" viewBox="0 0 82 82" aria-hidden="true"><path fill="var(--icon)" d="M41 2 L48 16 L62 6 L61 22 L78 20 L68 34 L80 44 L65 50 L72 66 L56 62 L52 80 L41 68 L30 80 L26 62 L10 66 L17 50 L2 44 L14 34 L4 20 L21 22 L20 6 L34 16 Z"/></svg>
    </span>
    <span class="menu-tile__label">Harmful Apps</span>
  </a>

  <a class="menu-tile tile-hot">
    <span class="menu-tile__icon">
      <svg width="60" height="80" viewBox="0 0 60 80" aria-hidden="true">
        <path fill="none" stroke="var(--icon)" stroke-width="5" stroke-linejoin="round" d="M14 4 C18 18 6 28 6 50 C6 66 17 76 30 76 C44 76 54 66 54 50 C54 38 48 28 44 22 C44 32 40 36 36 36 C38 24 28 12 14 4 Z"/>
        <path fill="none" stroke="var(--icon)" stroke-width="4" stroke-linejoin="round" d="M18 40 C20 48 14 54 16 62 C18 68 24 70 30 70 C38 70 44 64 44 56 C44 50 40 46 38 44 C38 50 34 52 32 52 C32 46 26 42 18 40 Z"/>
      </svg>
    </span>
    <span class="menu-tile__label">Hot Apps</span>
  </a>
</section>

<section class="screen screen--splash" aria-label="Loading splash">
  <svg class="splash-collage" width="524" height="210" viewBox="0 0 524 210" role="img" aria-label="Curved band filled with a collage of colourful app icons">
    <defs>
      <linearGradient id="collage-tones" x1="0" y1="0" x2="1" y2="1">
        <stop offset="0" stop-color="#3b4f6e"/>
        <stop offset=".35" stop-color="#5a6f4a"/>
        <stop offset=".65" stop-color="#6e4a3a"/>
        <stop offset="1" stop-color="#2e3440"/>
      </linearGradient>
    </defs>
    <path d="M0 0 H524 V55 C470 140 360 200 230 204 C130 206 50 190 0 170 Z" fill="url(#collage-tones)"/>
  </svg>

  <h2 class="splash-title">APP MANAGER</h2>

  <svg class="splash-globe" width="300" height="300" viewBox="0 0 300 300" role="img" aria-label="Sphere covered with colourful app icons">
    <defs>
      <radialGradient id="globe-tones" cx=".35" cy=".4" r=".7">
        <stop offset="0" stop-color="#ffffff"/>
        <stop offset=".5" stop-color="#dfe3ea"/>
        <stop offset="1" stop-color="#7f8896"/>
      </radialGradient>
    </defs>
    <circle cx="165" cy="175" r="160" fill="#262626"/>
    <circle cx="170" cy="180" r="146" fill="url(#globe-tones)"/>
  </svg>
</section>

</body>
</html>
```